Design a BOLD Ad Design for Fitness Club

We are fitness facility that is about to run our new "Bright Parent Reboot" program and we need a bold design created for an ad that will run on Instagram and Facebook.

The ad needs to be eye catching, easy to read and attractive so that someone stops scrolling and clicks to join.

The add needs to be sized to 1080 x 1080, include our logo and the text "Bright Parent Reboot" and "Starting September 23rd"

I have included an example photo, which is to be used as an example only of a design style that stands out to us, (colors, female photo style, etc)

I have also included our logo, which the yellow color can be changed for this design.

Thank you and we look forward to seeing your design.

```html
<!DOCTYPE html>
<html lang="en">
<head>
<meta charset="utf-8">
<title>Bright Parent Reboot – Ad</title>
<link rel="stylesheet" href="https://fonts.googleapis.com/css2?family=Archivo:ital,wdth,wght@1,62..125,900&family=Poppins:wght@600;700;800&display=swap">
<style>
  :root {
    --ink: #111111;
    --magenta: #f01fb2;
    --magenta-deep: #9c1378;
    --white: #ffffff;
    --skin: #c99a80;
    --hair: #6b4a35;
  }
  * { margin: 0; padding: 0; box-sizing: border-box; }
  html, body { width: 1200px; height: 1200px; overflow: hidden; background: var(--ink); }
  .ad {
    position: relative;
    width: 1200px;
    height: 1200px;
    background: var(--ink);
    overflow: hidden;
    font-family: "Poppins", sans-serif;
  }
  .glow-top {
    position: absolute; inset: 0;
    background:
      radial-gradient(ellipse 520px 420px at 1120px 180px, rgba(240,31,178,0.85), rgba(240,31,178,0.25) 55%, transparent 75%),
      radial-gradient(ellipse 420px 300px at 1180px 1160px, rgba(240,31,178,0.8), rgba(240,31,178,0.2) 55%, transparent 75%);
  }
  .athlete-photo {
    position: absolute;
    left: 560px; top: 74px;
    width: 640px; height: 1126px;
    border-radius: 260px 0 0 0;
    background: linear-gradient(180deg, var(--hair) 0%, var(--skin) 30%, #b78670 45%, #1b1b1b 55%, #151515 100%);
    opacity: 0.9;
  }
  .brand {
    position: absolute;
    left: 107px; top: 110px;
    width: 550px;
    text-align: center;
  }
  .brand-name {
    display: block;
    font-family: "Poppins", sans-serif;
    font-weight: 800;
    font-size: 112px;
    line-height: 1.1;
    letter-spacing: -2px;
    color: var(--white);
  }
  .brand-tagline {
    display: block;
    margin-top: 14px;
    font-weight: 700;
    font-size: 20px;
    letter-spacing: 4px;
    color: var(--magenta);
  }
  .headline {
    position: absolute;
    left: 90px; top: 330px;
    font-family: "Archivo", sans-serif;
    font-style: italic;
    font-weight: 900;
    font-stretch: 70%;
    font-size: 196px;
    line-height: 200px;
    text-transform: uppercase;
    color: var(--white);
  }
  .headline span { display: block; }
  .headline .line-outline {
    color: transparent;
    -webkit-text-stroke: 3px var(--white);
  }
  .date-banner {
    position: absolute;
    left: 80px; top: 970px;
    width: 882px; height: 128px;
  }
  .date-banner svg { position: absolute; inset: 0; }
  .date-text {
    position: absolute; inset: 0;
    display: flex; align-items: center; justify-content: center;
    font-weight: 700;
    font-size: 52px;
    color: var(--white);
    letter-spacing: 0.5px;
  }
  .chevrons { position: absolute; left: 1010px; top: 1016px; }
</style>
</head>
<body>
<main class="ad">
  <div class="glow-top"></div>
  <div class="athlete-photo" role="img" aria-label="Photo of a smiling athletic woman in a black crop top flexing her arm"></div>

  <header class="brand">
    <span class="brand-name">PulseForge</span>
    <span class="brand-tagline">PERSONAL GROUP TRAINING</span>
  </header>

  <h1 class="headline">
    <span class="line-solid">Bright</span>
    <span class="line-solid">Parent</span>
    <span class="line-outline">Reboot</span>
  </h1>

  <div class="date-banner">
    <svg width="882" height="128" viewBox="0 0 882 128" aria-hidden="true">
      <path d="M18 14 L860 6 L872 40 L882 62 L868 92 L874 118 L30 124 L6 112 L20 86 L0 60 L14 36 Z" fill="var(--magenta)"/>
    </svg>
    <p class="date-text">STARTING SEPTEMBER 23RD</p>
  </div>

  <svg class="chevrons" width="110" height="52" viewBox="0 0 110 52" aria-hidden="true">
    <g fill="none" stroke="var(--white)" stroke-width="4" stroke-linecap="round" stroke-linejoin="round">
      <polyline points="24,6 6,26 24,46"/>
      <polyline points="60,6 42,26 60,46"/>
      <polyline points="96,6 78,26 96,46"/>
    </g>
  </svg>
</main>
</body>
</html>
```